Ardenwell Building and Property Services needs a business card design

We need a business card design for our building and property services business. We already have a logo we just need a creative design and layout on a business card. Emphasis on clean, modern, professional.
Our client targets are mainly body corporates, building managers, construction managers.
We are a building services company that lean more to structural repair of buildings, through concrete rectification and carbon fibre strengthening.
We also refurbish facades, rendering, painting etc
We target higher end body corporates in prestigious locations, hence why we'd like our cards to reflect professionalism, strength, efficiency

Target Market(s)

body corporates, building managers, construction managers

Industry/Entity Type

Construction

Contact Information for Business Card

Ardenwell is the main word, with 'Building and Property Services' underneath.
Level 17, 82 Harlow Street
MERRIDALE
Melbourne
Vic 3094
T: 9518 2736
Duncan Ferris - Director
dunardenwell@mailbox-example.com

Requirements
Must have
• Stand out on the back of the card- strong/ bold, company logo
• All of the contact details written above
Should not have
• I'd like the card to stand out, especially on the back. Id like the company logo to be prominent, although feel free to be creative around it. But remain clean and professional

```html
<!DOCTYPE html>
<html lang="en">
<head>
<meta charset="utf-8">
<title>Ardenwell Building and Property Services – Business Card</title>
<link rel="stylesheet" href="https://fonts.googleapis.com/css2?family=Cinzel:wght@400;700&family=Crimson+Text:wght@400;700&display=swap">
<style>
  :root {
    --stage: #2e3034;
    --card-white: #ffffff;
    --blue-deep: #1d56a8;
    --blue-mid: #2a78c4;
    --blue-bright: #3aa3e0;
    --blue-light: #4fb4ea;
    --navy: #1a3f8a;
    --grey-text: #7a7f86;
    --white: #ffffff;
  }
  * { margin: 0; padding: 0; box-sizing: border-box; }
  html, body {
    width: 1200px;
    height: 900px;
    overflow: hidden;
    background: var(--stage);
  }
  .canvas {
    position: relative;
    width: 1200px;
    height: 900px;
    display: flex;
    flex-direction: column;
    align-items: center;
    justify-content: center;
    gap: 40px;
  }
  .card {
    position: relative;
    width: 640px;
    height: 366px;
    border-radius: 20px;
    overflow: hidden;
  }

  /* Back of card */
  .card-back {
    background: linear-gradient(135deg, var(--blue-bright) 0%, var(--blue-mid) 45%, var(--blue-deep) 100%);
    display: flex;
    flex-direction: column;
    align-items: center;
    justify-content: center;
    gap: 8px;
  }
  .card-back .brand-name {
    font-family: "Cinzel", serif;
    font-weight: 700;
    font-size: 58px;
    letter-spacing: 4px;
    color: var(--white);
    line-height: 1;
  }
  .card-back .brand-tagline {
    font-family: "Cinzel", serif;
    font-weight: 400;
    font-size: 15px;
    letter-spacing: 3px;
    color: #d6ecfa;
  }

  /* Front of card */
  .card-front { background: var(--card-white); }
  .card-front .band {
    position: absolute;
    inset: 0;
    width: 640px;
    height: 366px;
  }
  .card-front .brand {
    position: absolute;
    left: 36px;
    top: 34px;
  }
  .card-front .brand-name {
    font-family: "Cinzel", serif;
    font-weight: 400;
    font-size: 66px;
    letter-spacing: 3px;
    color: var(--blue-light);
    line-height: 1;
  }
  .card-front .brand-tagline {
    margin-top: 8px;
    font-family: "Cinzel", serif;
    font-size: 17px;
    letter-spacing: 3px;
    color: var(--grey-text);
  }
  .person {
    position: absolute;
    left: 40px;
    top: 168px;
    font-family: "Crimson Text", serif;
  }
  .person-name {
    font-weight: 700;
    font-size: 24px;
    letter-spacing: 0.5px;
    color: var(--navy);
    text-transform: uppercase;
  }
  .person-role {
    font-size: 15px;
    letter-spacing: 1px;
    color: var(--blue-bright);
    text-transform: uppercase;
  }
  .contact {
    position: absolute;
    left: 40px;
    top: 252px;
    font-family: "Crimson Text", serif;
    font-size: 16px;
    line-height: 24px;
    color: var(--white);
    list-style: none;
  }
  .contact li { display: flex; align-items: center; gap: 8px; }
  .contact .icon { width: 13px; height: 13px; flex: none; }
  .contact .plain { padding-left: 0; }
</style>
</head>
<body>
  <main class="canvas">
    <section class="card card-back" aria-label="Business card back">
      <div class="brand-name">ARDENWELL</div>
      <div class="brand-tagline">BUILDING AND PROPERTY SERVICES</div>
    </section>

    <section class="card card-front" aria-label="Business card front">
      <svg class="band" viewBox="0 0 640 366" aria-hidden="true">
        <defs>
          <linearGradient id="bandFill" x1="0" y1="1" x2="1" y2="0">
            <stop offset="0" stop-color="#1d56a8"/>
            <stop offset="1" stop-color="#3aa3e0"/>
          </linearGradient>
        </defs>
        <polygon points="0,238 420,238 500,150 640,150 640,366 0,366" fill="url(#bandFill)"/>
      </svg>

      <div class="brand">
        <div class="brand-name">ARDENWELL</div>
        <div class="brand-tagline">BUILDING AND PROPERTY SERVICES</div>
      </div>

      <div class="person">
        <div class="person-name">Duncan Ferris</div>
        <div class="person-role">Director</div>
      </div>

      <ul class="contact">
        <li class="plain">Level 17, 82 Harlow Street</li>
        <li class="plain">MERRIDALE , Melbourne Vic 3094</li>
        <li>
          <svg class="icon" viewBox="0 0 16 16" aria-hidden="true"><path d="M4 1l3 3-2 2c1 2 3 4 5 5l2-2 3 3-2 3C7 15 1 9 1 3z" fill="#bfe3fa"/></svg>
          9518 2736
        </li>
        <li>
          <svg class="icon" viewBox="0 0 16 16" aria-hidden="true"><rect x="1" y="3" width="14" height="10" rx="1" fill="none" stroke="#bfe3fa" stroke-width="1.6"/><path d="M1 4l7 5 7-5" fill="none" stroke="#bfe3fa" stroke-width="1.6"/></svg>
          dunardenwell@mailbox-example.com
        </li>
      </ul>
    </section>
  </main>
</body>
</html>
```